Business Card Design

I'm a commercial general contractor remodel offices, hotels, health clubs and stores mostly San Francisco and the peninsula
the file I down loaded is kind of what I want I like the I beam with my company name in it, that would be fine with me but if you have better Idea will look at it you never know, I'm decided to give in and change my company name to how every one knows me, I have been in business since 1991, I like the I beam logo I included one of my old card from my old company for reference for you.

Industry/Entity Type

Business

Contact Information for Business Card

BRAXO CONSTRUCTION (is my company name)
Wendell Trusk contractor, LIc 314827
4158 Garnet Row, Cedar Hollow, Nevada 89952
mobile, (555) 555-0147
phone (555) 555-0182
Fax, (555) 555-0183
email, braxo@braxoconstruction.example

```html
<!DOCTYPE html>
<html lang="en">
<head>
<meta charset="utf-8">
<title>Braxo Construction – Business Card</title>
<link href="https://fonts.googleapis.com/css2?family=Arimo:wght@700&family=Mali:wght@700&display=swap" rel="stylesheet">
<style>
  :root {
    --card-bg: #ffffff;
    --card-edge: #9a9a9a;
    --brand-blue: #1b8fdc;
    --rule-navy: #2b2171;
    --ink: #2a2a2a;
    --name-ink: #111111;
  }
  html, body {
    margin: 0;
    padding: 0;
    width: 1200px;
    height: 704px;
    overflow: hidden;
    background: var(--card-bg);
  }
  .card {
    position: relative;
    width: 1200px;
    height: 704px;
    box-sizing: border-box;
    border: 1px solid var(--card-edge);
    background: var(--card-bg);
    font-family: "Arimo", Arial, sans-serif;
    font-weight: 700;
    color: var(--ink);
  }
  .card > * { position: absolute; margin: 0; line-height: 1; white-space: nowrap; }

  .brand-name {
    left: 0; right: 0;
    top: 126px;
    text-align: center;
    font-size: 62px;
    letter-spacing: 1px;
    color: var(--brand-blue);
  }

  .person-name,
  .person-title {
    left: 49px;
    font-family: "Mali", "Comic Sans MS", cursive;
    font-size: 40px;
    color: var(--name-ink);
  }
  .person-name { top: 326px; }
  .person-title { top: 389px; }

  .divider {
    left: 24px;
    width: 1150px;
    top: 465px;
    height: 6px;
    background: var(--rule-navy);
  }

  .phone-list {
    left: 49px;
    top: 512px;
    padding: 0;
    list-style: none;
    font-size: 32px;
  }
  .phone-list li { height: 58px; display: flex; }
  .phone-label { width: 136px; }

  .contact-right {
    right: 49px;
    text-align: right;
    font-size: 32px;
  }
  .email { top: 493px; font-size: 31px; }
  .street { top: 550px; }
  .city { top: 595px; }
  .license { top: 652px; }
</style>
</head>
<body>
  <div class="card">
    <p class="brand-name">BRAXO CONSTRUCTION</p>

    <p class="person-name">Wendell Trusk</p>
    <p class="person-title">General Contractor</p>

    <div class="divider"></div>

    <ul class="phone-list">
      <li><span class="phone-label">Mobile:</span><span>(555) 555-0147</span></li>
      <li><span class="phone-label">Phone:</span><span>(555) 555-0182</span></li>
      <li><span class="phone-label">Fax:</span><span>(555) 555-0183</span></li>
    </ul>

    <p class="contact-right email">Email: braxo@braxoconstruction.example</p>
    <p class="contact-right street">4158 Garnet Row,</p>
    <p class="contact-right city">Cedar Hollow, Nevada 89952</p>
    <p class="contact-right license">Lic # 314827</p>
  </div>
</body>
</html>
```